Tri Fold - Restaurant Brochure & pdf multipage

Develop a product guide specific to "restaurant owners" for our company's restaurant insurance services. It will need to be eye-catching, personal, unique, and industry-specific. Several Insurance flyers from our companies are attached for review. We are happy to provide guidance along the way. Our website is www.kovalenbrokerage.example. Please grab logos etc. from there. We can provide other files and more detailed copy.

Target Market(s)

Restaurant owners and CFO's

Industry/Entity Type

Insurance Broker

Font styles to use
Other font styles liked:
• match website fonts

Requirements
Must have
• WE WILL PROVIDE DETAILED CONTENT! AT THIS TIME WE ARE LOOKING FOR THE BASIC DESIGN AND LAYOUT.

EYE-CATCHING MODERN DESIGN WITH IMAGES AND BRANDED FEEL. must be print-ready and set up as a PDF to email.

brief description of our agency and its personal boutique feel specializing in the restaurant market. Also, offer a full-service solution to no only manage their business but personal risks too.

Coverages that need to be listed with a brief description: (See attached Flyers)
General Liability
FF&E (Furniture, Fixtures, and Equipment), Property
Workers Compensation
Umbrella
Liquor Liability
Auto
Cyber
Bonds
EPLI

Carrier List:
The Wexmoor
Bastion
Ferrow Common
Wayfarers
Plains Motor
Quorra
DELVA
Holloway
CountyFirst
KTO
And many more
Nice to have
• carrier logos if room.
Should not have
• TO BE DETERMINED.

```html
<!DOCTYPE html>
<html lang="en">
<head>
<meta charset="utf-8">
<title>Kovalen Brokerage – Restaurant Tri-Fold</title>
<link href="https://fonts.googleapis.com/css2?family=Oswald:wght@500;700&family=Open+Sans:ital,wght@0,400;0,600;0,700;0,800;1,700&display=swap" rel="stylesheet">
<style>
:root{
  --red:#e8211d;
  --black:#111111;
  --white:#ffffff;
  --ink:#333333;
  --grey:#777777;
  --page:#eeeeee;
  --rule:#dddddd;
}
*{box-sizing:border-box;margin:0;padding:0}
html,body{width:669px;height:1200px;overflow:hidden}
body{background:var(--page);font-family:"Open Sans",Arial,sans-serif;color:var(--ink);position:relative}
.spread{position:absolute;left:20px;width:629px;height:348px;display:grid;grid-template-columns:repeat(3,1fr);background:var(--white);box-shadow:0 2px 6px rgba(0,0,0,.18)}
.spread--outside{top:232px}
.spread--inside{top:620px}
.panel{position:relative;overflow:hidden;padding:10px 11px;font-size:4.3px;line-height:1.45}
.panel--red{background:var(--red);color:var(--white)}
.panel--black{background:var(--black);color:var(--white);padding:0}
.panel--plain{padding:0}
p{margin-bottom:4px}
.icon-head{display:flex;align-items:center;gap:5px;font-weight:800;font-size:5.6px;margin:2px 0 5px;text-transform:uppercase}
.icon-dot{width:13px;height:13px;border-radius:50%;background:var(--white);flex:none;display:flex;align-items:center;justify-content:center}
.icon-dot--red{background:var(--red)}
.check-list{list-style:none;display:grid;grid-template-columns:1fr 1fr;gap:3px 6px;margin:4px 0 8px}
.check-list li{display:flex;gap:3px;align-items:flex-start}
.check-list li::before{content:"";width:4px;height:4px;border:0.6px solid currentColor;border-radius:50%;flex:none;margin-top:1px}
.contact-note{font-weight:700;font-size:4.6px;margin:6px 0}
.note-bar{background:var(--white);color:var(--red);font-weight:700;font-size:5px;padding:3px 5px;margin-bottom:7px}
.offices{display:grid;grid-template-columns:1fr 1fr;gap:6px}
.offices h4{font-size:5.6px;font-weight:700;margin-bottom:3px}
.offices .line{display:flex;gap:3px;align-items:flex-start;margin-bottom:3px}
.photo{display:block;width:100%}
.photo--sea{position:absolute;left:0;right:0;bottom:0;height:78px;background:linear-gradient(180deg,#e9a86a 0%,#c77b55 35%,#3c5d78 60%,#1f3850 100%)}
.photo--dining{height:132px;background:linear-gradient(135deg,#2c3a2c 0%,#5c4a36 45%,#a08a6a 75%,#3b3a33 100%)}
.photo--owner{height:132px;background:linear-gradient(160deg,#6f6c63 0%,#4b3a30 50%,#2a2420 100%)}
.photo--couple{height:70px;background:linear-gradient(120deg,#4a3e36 0%,#8b7562 50%,#cfc2b2 100%)}
.photo--house{height:58px;background:linear-gradient(180deg,#2f3e55 0%,#4f5e70 45%,#b98a55 70%,#3a3129 100%);margin-top:6px}
.brand{height:62px;display:flex;align-items:center;justify-content:center;gap:5px}
.brand--light{background:var(--white)}
.brand-mark{width:8px;height:8px;background:var(--red)}
.brand-name{font-family:"Oswald",Arial,sans-serif;font-weight:700;font-size:15px;letter-spacing:.5px;color:var(--black)}
.brand--dark .brand-name{color:var(--white)}
.contact{padding:10px 12px;text-align:center}
.contact h3{font-family:"Oswald",Arial,sans-serif;font-weight:500;color:var(--red);font-size:10px;letter-spacing:.4px;margin-bottom:9px}
.contact-item{display:flex;flex-direction:column;align-items:center;gap:3px;font-size:4.6px;font-weight:600;margin-bottom:8px;color:var(--ink)}
.contact-item::after{content:"";width:100%;height:0.5px;background:var(--rule);margin-top:4px}
.contact-item:last-child::after{display:none}
.cover{padding:12px 14px}
.cover h1{font-family:"Oswald",Arial,sans-serif;font-weight:700;font-size:21px;line-height:1;color:var(--white);letter-spacing:.3px}
.cover h2{font-family:"Oswald",Arial,sans-serif;font-weight:500;font-size:13px;color:var(--red);letter-spacing:1px;margin-bottom:8px}
.cover p{font-size:4.8px;text-align:center;margin-bottom:9px}
.pill{display:block;background:var(--red);color:var(--white);font-weight:700;font-size:4.8px;text-align:center;padding:3px 6px;border-radius:6px;margin:0 18px}
.band{background:var(--red);color:var(--white);font-family:"Oswald",Arial,sans-serif;font-weight:500;font-size:7.5px;line-height:1.15;text-align:center;padding:5px 8px;margin:0 14px;position:relative;top:-9px}
.serve{padding:0 11px}
.serve h3{color:var(--red);font-weight:700;font-size:7px;line-height:1.2;margin-bottom:5px}
.carriers{display:grid;grid-template-columns:1fr 1fr;gap:0 8px;margin-top:6px;font-size:4.6px}
.carriers li{list-style:none;padding:2.5px 0;border-bottom:0.5px solid var(--rule)}
.red-title{background:var(--red);color:var(--white);font-weight:800;font-size:5.4px;line-height:1.3;text-align:center;padding:4px 6px;margin-bottom:6px;text-transform:uppercase}
.cover-list{list-style:none;display:grid;grid-template-columns:1fr 1fr;gap:3px 6px;font-size:4.6px;margin-bottom:8px}
.cover-list li{display:flex;gap:3px;align-items:flex-start}
.cover-list li::before{content:"";width:3px;height:3px;background:var(--red);border-radius:50%;flex:none;margin-top:1.2px}
.lead-italic{color:var(--red);font-style:italic;font-weight:700;font-size:4.8px;margin-bottom:3px}
.bullets{list-style:none;margin-bottom:5px}
.bullets li{display:flex;gap:3px;margin-bottom:2px}
.bullets li::before{content:"";width:3px;height:3px;background:var(--red);flex:none;margin-top:1.2px}
.lead{color:var(--red);font-weight:700}
.optional{display:flex;margin:6px 0 5px}
.optional .left{flex:1.2;background:var(--black);color:var(--white);font-weight:700;font-size:4.4px;line-height:1.25;padding:3px 5px;text-transform:uppercase}
.optional .right{flex:1;background:var(--red);color:var(--white);font-family:"Oswald",Arial,sans-serif;font-weight:500;font-size:7.5px;display:flex;align-items:center;justify-content:center}
.markets{font-weight:700;font-size:5.4px;margin-bottom:3px;color:var(--black)}
.icon-head--red{color:var(--red);font-size:5.4px}
.tick-list{list-style:none;display:grid;grid-template-columns:1fr 1fr;gap:3px 6px}
.tick-list li{display:flex;gap:3px;align-items:center}
.tick-list svg{flex:none}
</style>
</head>
<body>

<!-- Outside spread -->
<section class="spread spread--outside">
  <div class="panel panel--red">
    <div class="icon-head"><span class="icon-dot"><svg width="7" height="7" viewBox="0 0 10 10"><rect x="1.5" y="4.5" width="7" height="5" fill="#e8211d"/><path d="M3 4.5V3a2 2 0 0 1 4 0v1.5" stroke="#e8211d" fill="none" stroke-width="1.2"/></svg></span>24/7 My Account Access</div>
    <p>Our clients enjoy around the clock online access to a number of self-service options and account tools.</p>
    <ul class="check-list">
      <li>Pay online day or night by card or bank draft</li>
      <li>Send an electronic claim directly to your carrier</li>
      <li>Print your own insurance ID cards anytime</li>
      <li>Request a Certificate of Insurance instantly</li>
      <li>Review all policies in one place</li>
      <li>Track open claims and policy updates</li>
    </ul>
    <div class="icon-head"><span class="icon-dot"><svg width="8" height="7" viewBox="0 0 12 10"><rect x="1" y="3" width="10" height="4" rx="1" fill="#e8211d"/><circle cx="3.5" cy="8" r="1.3" fill="#e8211d"/><circle cx="8.5" cy="8" r="1.3" fill="#e8211d"/><path d="M3 3l1.5-2h3L9 3" fill="#e8211d"/></svg></span>Business Auto</div>
    <p>Business auto policies cover vehicles owned, leased or used by your restaurant, including delivery and catering runs. Hired and non-owned protection is available for employees who drive their own cars on the job.</p>
    <p class="contact-note">Contact Info – www.servesafecover.example – owned by Kovalen Brokerage LLC www.kovalenbrokerage.example</p>
    <div class="note-bar">List both locations and my direct contact info</div>
    <div class="offices">
      <div>
        <h4>Brookhaven</h4>
        <div class="line"><svg width="5" height="5" viewBox="0 0 10 10"><path d="M2 1h2l1 2.5-1.2 1a6 6 0 0 0 2.7 2.7l1-1.2L10 7v2a1 1 0 0 1-1 1A9 9 0 0 1 0 2a1 1 0 0 1 1-1z" fill="#fff"/></svg>555-014-2210</div>
        <div class="line"><svg width="5" height="5" viewBox="0 0 10 10"><path d="M5 0a3.5 3.5 0 0 1 3.5 3.5C8.5 6 5 10 5 10S1.5 6 1.5 3.5A3.5 3.5 0 0 1 5 0z" fill="#fff"/></svg>48 Orchard Row<br>Brookhaven, ST 30100</div>
      </div>
      <div>
        <h4>Linden Falls</h4>
        <div class="line"><svg width="5" height="5" viewBox="0 0 10 10"><path d="M2 1h2l1 2.5-1.2 1a6 6 0 0 0 2.7 2.7l1-1.2L10 7v2a1 1 0 0 1-1 1A9 9 0 0 1 0 2a1 1 0 0 1 1-1z" fill="#fff"/></svg>555-018-7734</div>
        <div class="line"><svg width="5" height="5" viewBox="0 0 10 10"><path d="M5 0a3.5 3.5 0 0 1 3.5 3.5C8.5 6 5 10 5 10S1.5 6 1.5 3.5A3.5 3.5 0 0 1 5 0z" fill="#fff"/></svg>902 Mill Court Suite 4<br>Linden Falls, ST 27400</div>
      </div>
    </div>
    <div class="photo photo--sea" role="img" aria-label="Photo of a boat wake on open water at sunset"></div>
  </div>

  <div class="panel panel--plain">
    <div class="brand brand--light"><span class="brand-mark"></span><span class="brand-name">KOVALEN BROKERAGE</span></div>
    <div class="photo photo--dining" role="img" aria-label="Photo of a restaurant dining room seen through glass"></div>
    <div class="contact">
      <h3>CONTACT US</h3>
      <div class="contact-item"><span class="icon-dot icon-dot--red"><svg width="7" height="7" viewBox="0 0 10 10"><path d="M2 1h2l1 2.5-1.2 1a6 6 0 0 0 2.7 2.7l1-1.2L10 7v2a1 1 0 0 1-1 1A9 9 0 0 1 0 2a1 1 0 0 1 1-1z" fill="#fff"/></svg></span>555-014-2210</div>
      <div class="contact-item"><span class="icon-dot icon-dot--red"><svg width="7" height="7" viewBox="0 0 10 10"><rect x="0.5" y="2" width="9" height="6" fill="#fff"/><path d="M0.5 2L5 5.5 9.5 2" stroke="#e8211d" stroke-width="0.8" fill="none"/></svg></span>info@kovalenbrokerage.example</div>
      <div class="contact-item"><span class="icon-dot icon-dot--red"><svg width="7" height="7" viewBox="0 0 10 10"><circle cx="5" cy="5" r="4" stroke="#fff" fill="none" stroke-width="0.9"/><ellipse cx="5" cy="5" rx="1.8" ry="4" stroke="#fff" fill="none" stroke-width="0.7"/><path d="M1 5h8" stroke="#fff" stroke-width="0.7"/></svg></span>www.kovalenbrokerage.example</div>
    </div>
  </div>

  <div class="panel panel--black">
    <div class="brand brand--dark"><span class="brand-mark"></span><span class="brand-name">KOVALEN BROKERAGE</span></div>
    <div class="photo photo--owner" role="img" aria-label="Photo of a restaurant owner in an apron standing with arms crossed"></div>
    <div class="cover">
      <h1>INDEPENDENT</h1>
      <h2>RISK ADVISORS</h2>
      <p>Kovalen Brokerage believes in the ability of people to take control of their lives and of their future.</p>
      <span class="pill">www.kovalenbrokerage.example</span>
    </div>
  </div>
</section>

<!-- Inside spread -->
<section class="spread spread--inside">
  <div class="panel panel--plain">
    <div class="photo photo--couple" role="img" aria-label="Photo of two diners talking at a restaurant table"></div>
    <div class="band">KOVALEN BROKERAGE<br>KNOWS RESTAURANTS!</div>
    <div class="serve">
      <h3>You work hard serving others here's how we can serve you.</h3>
      <p>Starting in the restaurant business is exciting. Running it is demanding. Finding coverage that truly fits a busy kitchen and a full dining room should not be. We take time to learn how your place works before we recommend a single policy.</p>
      <p>As a boutique agency focused on restaurants, we compare many markets to build a plan around your menu, staff and hours. We also look after the personal side, from home and auto to umbrella, so owners have one trusted team.</p>
      <p>Different restaurants face different risks. Whether you run a café, a bar or a fine dining room, we shape protection to match and review it as you grow.</p>
      <ul class="carriers">
        <li>The Wexmoor</li><li>Quorra</li>
        <li>Bastion</li><li>DELVA</li>
        <li>Ferrow Common</li><li>Holloway</li>
        <li>Wayfarers</li><li>CountyFirst</li>
        <li>Plains Motor</li><li>KTO</li>
      </ul>
    </div>
  </div>

  <div class="panel">
    <div class="red-title">Common coverages that need to be listed with a brief description:</div>
    <ul class="cover-list">
      <li>General Liability</li><li>Liquor Liability</li>
      <li>FF&amp;E (Furniture, Fixtures, and Equipment), Property</li><li>Auto</li>
      <li>Workers Compensation</li><li>Cyber</li>
      <li>Umbrella</li><li>Bonds</li>
      <li></li><li>EPLI</li>
    </ul>
    <div class="red-title">Business Owner's Policy (BOP)</div>
    <p>A BOP can help protect your business in much the same way that a homeowners policy protects your home and possessions. The BOP combines these essential coverages in one package.</p>
    <p class="lead-italic">A cost effective solution to help safeguard your restaurant</p>
    <ul class="bullets">
      <li>Business Property insurance to help protect the property you own or rent.</li>
      <li>Business Liability coverage to help protect your business if it is found responsible for an injury.</li>
      <li>Business Income coverage to replace lost income if a covered loss forces you to close.</li>
    </ul>
    <p><span class="lead">Data Breach</span> helps you pay for response expenses, legal costs and notices if customer or employee data is lost or stolen.</p>
    <p><span class="lead">Employment Practices Liability (EPLI)</span> provides coverage if you are sued by an employee over claims such as wrongful termination or harassment.</p>
    <p><span class="lead">Liquor Liability</span> helps cover your legal costs and damages if a guest you served causes injury or harm.</p>
    <p><span class="lead">Franchise Upgrade</span> helps you add protection that meets franchise requirements for a covered loss.</p>
    <p><span class="lead">Business Income for Food Contamination</span> provides coverage for lost income if your operation is suspended by a health authority.</p>
  </div>

  <div class="panel">
    <p><span class="lead">Business Income for Cloud Service Interruption</span> helps pay for lost income if you need to stop business operations because of an outage of a key online service you rely on.</p>
    <p><span class="lead">Employee Dishonesty</span> provides coverage if an employee steals money, securities or other property owned by your business.</p>
    <p><span class="lead">Spoilage</span> provides coverage for the cost of food or stock that is lost due to a breakdown or failure of heating or cooling equipment.</p>
    <p><span class="lead">Electronic Data and Interruption of Computer Operations</span> pays to replace or restore data that has been destroyed, corrupted, or made inaccessible.</p>
    <div class="optional"><div class="left">Our optional coverages don't stop here.</div><div class="right">CALL US TODAY</div></div>
    <div class="markets">Many markets offer:</div>
    <div class="icon-head icon-head--red"><span class="icon-dot icon-dot--red"><svg width="7" height="7" viewBox="0 0 10 10"><circle cx="5" cy="3" r="2" fill="#fff"/><path d="M1.5 10a3.5 3.5 0 0 1 7 0z" fill="#fff"/></svg></span>Workers' Compensation</div>
    <p>Your employees are important to the success of your restaurant. If an employee gets injured on the job, you can count on us to help cover their medical care and lost wages.</p>
    <div class="icon-head icon-head--red"><span class="icon-dot icon-dot--red"><svg width="7" height="7" viewBox="0 0 10 10"><rect x="1" y="2.5" width="8" height="5" rx="0.8" fill="#fff"/><rect x="1" y="3.8" width="8" height="1" fill="#e8211d"/></svg></span><span>Payroll Billing<br><span style="color:#333;font-weight:600;text-transform:none;font-size:4.3px">Helps improve the cash flow of your business.</span></span></div>
    <ul class="tick-list">
      <li><svg width="5" height="5" viewBox="0 0 10 10"><path d="M1.5 5.5l2.5 2.5 4.5-6" stroke="#e8211d" stroke-width="1.6" fill="none"/></svg>$0 deposit payment</li>
      <li><svg width="5" height="5" viewBox="0 0 10 10"><path d="M1.5 5.5l2.5 2.5 4.5-6" stroke="#e8211d" stroke-width="1.6" fill="none"/></svg>No surprise audits</li>
      <li><svg width="5" height="5" viewBox="0 0 10 10"><path d="M1.5 5.5l2.5 2.5 4.5-6" stroke="#e8211d" stroke-width="1.6" fill="none"/></svg>Pay as you go billing</li>
      <li><svg width="5" height="5" viewBox="0 0 10 10"><path d="M1.5 5.5l2.5 2.5 4.5-6" stroke="#e8211d" stroke-width="1.6" fill="none"/></svg>Simple online setup</li>
    </ul>
    <div class="photo photo--house" role="img" aria-label="Photo of a lit suburban home at dusk"></div>
  </div>
</section>

</body>
</html>
```